The Quillmore Daily Ledger

I am making a journal for tracking pain symptoms for TMJ (Jaw) pain. I have the cover designed and I just need the journal page designed that will repeat throughout the journal. The journal is the image on the left of the bundle. The page I would like to be developed is the picture that I hand sketched out. It should be a 6 x 9 page, similar to the attached example. Greyscale, no color. Thank you!

Target Market(s)

20-55 year old women

Industry/Entity Type

Healthcare

Colors

Designer to choose only greyscale colors for use in the design.

Requirements
Must have
• A neat, well-designed page with the content I have sketched out by hand.
Nice to have
• Creative display of the content I provided and development of the pain scale and pain diagram faces in a professional looking way.

```html
<!DOCTYPE html>
<html lang="en">
<head>
<meta charset="utf-8">
<title>The Quillmore Daily Ledger – Daily Page</title>
<link href="https://fonts.googleapis.com/css2?family=Arimo&family=Oswald:wght@400&family=Open+Sans:wght@400;600&display=swap" rel="stylesheet">
<style>
  :root {
    --backdrop: #f4f4f4;
    --paper: #ffffff;
    --paper-edge: #cfcfcf;
    --ink: #2a2a2a;
    --ink-soft: #555555;
    --brand: #6a6a6a;
    --band-dark: #b4b4b5;
    --band-light: #e6e6e6;
    --cell: #ececec;
    --panel: #f5f5f5;
    --box-line: #6d6d6d;
    --face-fill: #ececec;
    --face-ring: #9a9a9a;
    --art: #b9b9b9;
  }
  * { box-sizing: border-box; margin: 0; padding: 0; }
  html, body { width: 883px; height: 1200px; overflow: hidden; background: var(--backdrop); }
  body { position: relative; font-family: "Open Sans", sans-serif; color: var(--ink); }

  .page { position: absolute; left: 41px; top: 0; width: 800px; height: 1200px; background: var(--paper); border: 1px solid var(--paper-edge); }
  .abs { position: absolute; }

  /* brand */
  .brand { left: 0; width: 800px; top: 30px; display: flex; justify-content: center; align-items: center; gap: 10px; }
  .brand-dot { width: 40px; height: 40px; border-radius: 50%; border: 3px solid var(--brand); }
  .brand-name { font-family: "Open Sans", sans-serif; font-weight: 600; font-size: 17px; color: var(--brand); }

  /* date row */
  .field { font-family: "Arimo", sans-serif; font-size: 15.5px; color: var(--ink); display: flex; align-items: flex-end; top: 113px; }
  .field .rule { border-bottom: 1px solid var(--ink); margin-left: 2px; height: 16px; }
  .field-date { left: 62px; } .field-date .rule { width: 168px; }
  .field-day { left: 362px; } .field-day .rule { width: 224px; }

  /* band headings */
  .band { left: 64px; width: 672px; text-align: center; font-family: "Oswald", sans-serif; font-size: 16px; color: var(--ink); }
  .band.dark { background: var(--band-dark); }
  .band.light { background: var(--band-light); }
  .band small { font-family: "Open Sans", sans-serif; font-size: 14.5px; }

  /* time table */
  .time-title { top: 72px; }
  .time-band { top: 160px; height: 22px; line-height: 22px; font-family: "Arimo", sans-serif; font-size: 18px; }
  .time-table { position: absolute; left: 63px; top: 184px; width: 674px; border-collapse: separate; border-spacing: 2px; font-family: "Open Sans", sans-serif; font-size: 14px; color: var(--ink-soft); }
  .time-table th { background: var(--band-dark); font-weight: 400; height: 24px; }
  .time-table td { background: var(--cell); height: 26px; }
  .time-table .num { text-align: left; padding-left: 18px; font-family: "Oswald", sans-serif; color: var(--ink); }

  /* severity */
  .sev-band { top: 307px; height: 29px; line-height: 29px; }
  .sev-panel { left: 64px; top: 336px; width: 672px; height: 130px; background: var(--panel); }
  .sev-num { top: 343px; font-family: "Oswald", sans-serif; font-size: 23px; transform: translateX(-50%); }
  .face { width: 62px; height: 62px; border-radius: 50%; background: var(--face-fill); border: 2.5px solid var(--face-ring); top: 372px; transform: translateX(-50%); }
  .sev-label { top: 441px; font-size: 13.5px; transform: translateX(-50%); white-space: nowrap; }

  /* location */
  .loc-band { top: 480px; height: 29px; line-height: 29px; }
  .loc-panel { left: 64px; top: 510px; width: 377px; height: 132px; background: var(--paper); border: 2px solid var(--band-light); }
  .art { top: 528px; width: 60px; height: 84px; background: var(--art); border-radius: 6px; transform: translateX(-50%); }
  .art.teeth { top: 548px; height: 38px; border-radius: 14px; }
  .loc-label { top: 613px; font-size: 13.5px; transform: translateX(-50%); }
  .opt-panel { top: 512px; height: 130px; background: var(--panel); }
  .opt-head { top: 519px; height: 33px; line-height: 33px; text-align: center; font-family: "Oswald", sans-serif; font-size: 15.5px; background: var(--band-light); }
  .opt-list { list-style: none; }
  .opt-list li { height: 23px; display: flex; align-items: center; gap: 11px; font-size: 15px; }

  .box { display: inline-block; width: 13px; height: 13px; border: 1.2px solid var(--box-line); background: var(--paper); flex: none; }

  /* checklists */
  .list-band { height: 28px; line-height: 28px; }
  .list-panel { left: 64px; width: 672px; background: var(--panel); display: grid; grid-template-columns: 213px 236px 223px; }
  .list-panel ul { list-style: none; padding-left: 42px; padding-top: 10px; }
  .list-panel ul + ul { border-left: 1.5px solid var(--band-dark); padding-left: 37px; }
  .list-panel ul:last-child { padding-left: 23px; }
  .list-panel li { height: 23px; display: flex; align-items: center; gap: 14px; font-size: 15px; white-space: nowrap; }
  .list-panel li.tight { font-family: "Oswald", sans-serif; font-size: 14px; letter-spacing: -0.2px; }
  .blank { display: inline-block; border-bottom: 1px solid var(--ink); height: 14px; }

  .trig-band { top: 656px; }
  .trig-panel { top: 685px; height: 104px; }
  .relief-band { top: 876px; }
  .relief-panel { top: 904px; height: 105px; }

  /* state lines */
  .state { left: 86px; font-size: 15px; display: flex; align-items: center; gap: 4px; white-space: nowrap; }
  .state .box { margin-left: 10px; }

  /* notes */
  .notes-band { top: 1022px; }
  .notes-area { left: 64px; top: 1050px; width: 672px; height: 127px; border: 2px solid var(--band-light); display: grid; grid-template-rows: repeat(4, 1fr); }
  .notes-area span { border-bottom: 2px solid var(--band-light); }
  .notes-area span:last-child { border-bottom: none; }
</style>
</head>
<body>
<main class="page">

  <header class="abs brand">
    <span class="brand-dot"></span>
    <span class="brand-name">The Quillmore Daily Ledger</span>
  </header>

  <div class="abs field field-date">DATE <span class="rule"></span></div>
  <div class="abs field field-day">DAY OF THE WEEK<span class="rule"></span></div>

  <!-- time -->
  <div class="abs band light time-band">TIME</div>
  <table class="time-table">
    <colgroup><col style="width:49px"><col style="width:99px"><col style="width:99px"><col style="width:83px"><col style="width:51px"><col style="width:101px"><col style="width:96px"><col style="width:82px"></colgroup>
    <tr><th></th><th>begin</th><th>end</th><th>duraion</th><th></th><th>begin</th><th>end</th><th>duraion</th></tr>
    <tr><td class="num">1</td><td></td><td></td><td></td><td class="num">4</td><td></td><td></td><td></td></tr>
    <tr><td class="num">2</td><td></td><td></td><td></td><td class="num">5</td><td></td><td></td><td></td></tr>
    <tr><td class="num">3</td><td></td><td></td><td></td><td class="num">6</td><td></td><td></td><td></td></tr>
  </table>

  <!-- severity -->
  <div class="abs band dark sev-band">SEVERITY OF PAIN <small>(circle range)</small></div>
  <div class="abs sev-panel"></div>
  <span class="abs sev-num" style="left:108px">1</span>
  <span class="abs sev-num" style="left:169px">2</span>
  <span class="abs sev-num" style="left:232px">3</span>
  <span class="abs sev-num" style="left:294px">4</span>
  <span class="abs sev-num" style="left:357px">5</span>
  <span class="abs sev-num" style="left:419px">6</span>
  <span class="abs sev-num" style="left:481px">7</span>
  <span class="abs sev-num" style="left:544px">8</span>
  <span class="abs sev-num" style="left:607px">9</span>
  <span class="abs sev-num" style="left:676px">10</span>

  <div class="abs face" style="left:136px" role="img" aria-label="Pain scale icon: no pain"></div>
  <div class="abs face" style="left:241px" role="img" aria-label="Pain scale icon: mild pain"></div>
  <div class="abs face" style="left:347px" role="img" aria-label="Pain scale icon: moderate pain"></div>
  <div class="abs face" style="left:452px" role="img" aria-label="Pain scale icon: severe pain"></div>
  <div class="abs face" style="left:557px" role="img" aria-label="Pain scale icon: very severe pain"></div>
  <div class="abs face" style="left:662px" role="img" aria-label="Pain scale icon: worst pain possible"></div>

  <span class="abs sev-label" style="left:241px;top:445px">mild</span>
  <span class="abs sev-label" style="left:347px;top:445px">moderate</span>
  <span class="abs sev-label" style="left:452px;top:445px">severe</span>
  <span class="abs sev-label" style="left:557px">very severe</span>
  <span class="abs sev-label" style="left:662px">worst pain posible</span>

  <!-- location -->
  <div class="abs band dark loc-band">LOCATION</div>
  <div class="abs loc-panel"></div>
  <div class="abs art" style="left:107px" role="img" aria-label="Side-view head illustration highlighting the jaw joint"></div>
  <div class="abs art" style="left:182px" role="img" aria-label="Head illustration highlighting the jaw muscles"></div>
  <div class="abs art" style="left:252px" role="img" aria-label="Head illustration highlighting the neck"></div>
  <div class="abs art" style="left:321px" role="img" aria-label="Front-view head illustration highlighting forehead tension"></div>
  <div class="abs art teeth" style="left:396px" role="img" aria-label="Illustration of a set of teeth"></div>
  <span class="abs loc-label" style="left:107px">jmt</span>
  <span class="abs loc-label" style="left:182px">muscles</span>
  <span class="abs loc-label" style="left:252px">neck</span>
  <span class="abs loc-label" style="left:321px">tension</span>
  <span class="abs loc-label" style="left:396px">teeth</span>

  <div class="abs opt-panel" style="left:443px;width:130px"></div>
  <div class="abs opt-head" style="left:443px;width:130px">CLICK/POP</div>
  <ul class="abs opt-list" style="left:458px;top:558px">
    <li><span class="box"></span>increased</li>
    <li><span class="box"></span>decreased</li>
    <li><span class="box"></span>no change</li>
  </ul>
  <div class="abs opt-panel" style="left:575px;width:163px"></div>
  <div class="abs opt-head" style="left:575px;width:163px">OPENING ABILITY</div>
  <ul class="abs opt-list" style="left:591px;top:558px">
    <li><span class="box"></span>increased</li>
    <li><span class="box"></span>decreased</li>
    <li><span class="box"></span>no change</li>
  </ul>

  <!-- triggers -->
  <div class="abs band light list-band trig-band">TRIGGERS <small>(check all that apply)</small></div>
  <div class="abs list-panel trig-panel">
    <ul>
      <li><span class="box"></span>Sleep</li>
      <li><span class="box"></span>First thing in AM</li>
      <li><span class="box"></span>Clenching</li>
      <li><span class="box"></span>Insomnia</li>
    </ul>
    <ul>
      <li><span class="box"></span>Weather</li>
      <li><span class="box"></span>Eating</li>
      <li><span class="box"></span>Work</li>
      <li><span class="box"></span>Opening wide yawn</li>
    </ul>
    <ul>
      <li><span class="box"></span>PMS/menstration</li>
      <li><span class="box"></span>Stress at home</li>
      <li><span class="box"></span>Stress at work</li>
      <li><span class="box"></span>Other <span class="blank" style="width:110px;margin-left:-8px"></span></li>
    </ul>
  </div>

  <div class="abs state" style="top:799px">My saw was <span class="box"></span>relaxed <span class="box" style="margin-left:18px"></span>&nbsp;clenched</div>
  <div class="abs state" style="top:822px">My breath was <span class="box"></span>shallow/tense <span class="box" style="margin-left:18px"></span>&nbsp;deep/relaxed</div>
  <div class="abs state" style="top:845px">My neck/shalders were <span class="box" style="margin-left:4px"></span>relaxed <span class="box" style="margin-left:18px"></span>&nbsp;tense</div>

  <!-- relief -->
  <div class="abs band light list-band relief-band">RELIEF MEASURES <small>(check all that apply)</small></div>
  <div class="abs list-panel relief-panel">
    <ul>
      <li><span class="box"></span>Deep breathing</li>
      <li class="tight"><span class="box"></span>Teeth apart/relax/jaw</li>
      <li><span class="box"></span>Self-massage</li>
      <li><span class="box"></span>Heat/cold(circle)</li>
    </ul>
    <ul>
      <li><span class="box"></span>Medication</li>
      <li><span class="box"></span>Rest</li>
      <li><span class="box"></span>Gentle Stretching</li>
      <li><span class="box"></span>Positive correction</li>
    </ul>
    <ul>
      <li><span class="box"></span>Mindful reset</li>
      <li><span class="box"></span>Stabilization Exercise</li>
      <li><span class="box"></span>Other <span class="blank" style="width:110px;margin-left:-8px"></span></li>
      <li><span class="box"></span><span class="blank" style="width:158px"></span></li>
    </ul>
  </div>

  <!-- notes -->
  <div class="abs band light list-band notes-band">NOTES AND PLAN TO AVOID TRIGGERS</div>
  <div class="abs notes-area"><span></span><span></span><span></span><span></span></div>

</main>
</body>
</html>
```